Crest Cellarist - Make Your Own Wine at Home

We need a Tall Ledger design for a new commerce website based in Minneapolis call CrestCellarist. We sell equipment and supplies that enable anyone to make great wines at home. We support one's success as a wine maker with recipes, ingredients and equipment designed to never let you fail. We provide the know-how you need with step-by-step instructions, blogs and video classes. The final design should reflect the established Crest Cellarist product style as evidenced in the photos. It should appeal to both men and women "makers" who tend to be well educated and technical (designers, engineers, chemists, etc.) It should integrate commerce seamlessly with the learning community in a single site. It should give you confidence that "you can do this well" and "impress your friends" with the wine you made at home.

In order to understand the product line, see

http://www.quillfermentry.com/shop/winemaking

http://www.plainsgoodsdepot.com/winemaking-equipment.html
http://www.plainsgoodsdepot.com/winemaking-ingredients.html

http://www.jolvantic.com/

The deliverables will include psd files for home page, category page, product page and any connect, learn, video and or blog pages you propose as part of the UX/UI.

Target Market(s)

People who make wine, people interested in edible crafts including home brewing and distilling, cheesemaking, coffee roasting, baking, etc. People who love wine and craft beer but did not realize they could make their own.

Industry/Entity Type

Call

Font styles to use
Sans Serif

Requirements
Must have
• Project must reflect best practices in UX and UI design. It must anticipate responsive design application for multiple viewing devices. It must reflect Tall Ledger advantages and constraints.
Nice to have
• It should be personality driven (http://www.plainsgoodsdepot.com/oren-haselbeck/) but personable and approachable. Winemaking tends to be a community of like minded individuals seeking or sharing experience, technique and success. Navigation should be simple and intuitive (http://www.fondcasking.co.uk). It should be responsive to the questions of "where is it" (site search), "what do you think about" (reviews), "do you know" (questions and answers).
Should not have
• This should not be whimsical or playful. Making good beer or wine requires discipline -- nobody is proud of a bad batch. It should not be disorganized. It should not reflect confusion as to style (too many colors, fonts or other design elements).

```html
<!DOCTYPE html>
<html lang="en">
<head>
<meta charset="utf-8">
<title>Crest Cellarist – Our Products</title>
<link href="https://fonts.googleapis.com/css2?family=Arimo:wght@400;700&family=Noto+Serif:ital,wght@0,400;0,700;1,400&display=swap" rel="stylesheet">
<style>
:root{
  --green:#2f8a55;
  --green-bright:#2fc46a;
  --green-foot:#5f9f56;
  --green-foot-dark:#4b8544;
  --brown:#3d3322;
  --text:#3a3a3a;
  --muted:#555;
  --page:#f1f1f1;
  --line:#bfbfbf;
  --white:#fff;
}
*{box-sizing:border-box;margin:0;padding:0}
html,body{width:1046px;height:1200px;overflow:hidden;background:var(--page)}
body{font-family:"Arimo",Arial,sans-serif;color:var(--text)}
.site{position:relative;width:1200px;height:1377px;transform:scale(.871667);transform-origin:0 0;background:var(--page)}
.topbar{position:absolute;left:0;top:0;width:1200px;height:35px;background:var(--green);border-bottom:1px solid #1f6a3e}
.topbar__phone{position:absolute;left:762px;top:8px;color:var(--white);font-size:14px;display:flex;align-items:center;gap:8px}
.topbar__social{position:absolute;left:933px;top:5px;display:flex;gap:10px}
.topbar__social span{width:24px;height:24px;border-radius:50%;background:var(--white);display:block}
.nav{position:absolute;left:0;top:35px;width:1200px;height:68px;background:linear-gradient(#f7f7f7,#dcdcdc)}
.nav a{position:absolute;top:25px;font-family:"Noto Serif",Georgia,serif;font-size:14px;color:#222;text-decoration:none;letter-spacing:.3px}
.nav a.is-active{top:19px;background:#14201a;color:var(--white);border-radius:7px;padding:5px 11px;font-weight:700}
.brand{position:absolute;left:106px;top:2px;width:181px;height:181px;border-radius:50%;background:var(--white);box-shadow:0 2px 5px rgba(0,0,0,.25);display:flex;align-items:center;justify-content:center;z-index:2}
.brand__disc{width:160px;height:160px;border-radius:50%;background:#222;display:flex;align-items:center;justify-content:center;text-align:center;font-family:"Noto Serif",Georgia,serif;font-weight:700;font-size:24px;line-height:1.15;color:#e8e8e8}
.hero{position:absolute;left:0;top:103px;width:1200px;height:202px;background:radial-gradient(ellipse at 30% 40%,#c99a62 0%,#8a5a33 40%,#3d2515 80%),#5a3a22}
.hero__text{position:absolute;left:698px;top:72px;font-family:"Noto Serif",Georgia,serif;color:var(--white);text-shadow:0 2px 4px rgba(0,0,0,.6)}
.hero__line1{font-size:33px;letter-spacing:1px}
.hero__line2{font-size:42px;font-weight:700;color:var(--green-bright);letter-spacing:2px;line-height:1}
.breadcrumb{position:absolute;left:104px;top:320px;font-size:13px;color:#111}
.panel{position:absolute;left:100px;width:233px;background:var(--white);border:1px solid #e2e2e2;padding:6px 20px 0 18px}
.panel h2{font-family:"Noto Serif",Georgia,serif;font-size:29px;color:var(--green);font-weight:700;margin-bottom:12px}
.panel li{list-style:none;font-size:14px;color:var(--text);height:32px;line-height:30px;border-bottom:1px dashed var(--line);padding-left:15px;position:relative;letter-spacing:.2px;white-space:nowrap;overflow:visible}
.panel li:last-child{border-bottom:none}
.panel li::before{content:"";position:absolute;left:2px;top:11px;border-left:4px solid #555;border-top:4px solid transparent;border-bottom:4px solid transparent}
.panel--cats{top:353px;height:381px}
.panel--posts{top:761px;height:380px}
.products-head{position:absolute;left:371px;top:357px;width:727px;height:40px;background:var(--green);display:flex;align-items:center;justify-content:space-between;padding:0 12px 0 15px;color:var(--white)}
.products-head h1{font-family:"Noto Serif",Georgia,serif;font-size:28px;font-weight:700}
.pager{font-size:18px;display:flex;gap:10px}
.card{position:absolute;width:212px;height:222px;background:var(--white);border:1px solid #e3e3e3;padding:10px}
.card__img{display:block;width:190px;height:134px}
.card__name{font-size:14px;color:var(--muted);margin:12px 0 0 6px;letter-spacing:.2px;white-space:nowrap}
.card__foot{display:flex;justify-content:space-between;align-items:center;margin-top:12px;padding-left:6px}
.card__price{color:var(--green);font-weight:700;font-size:14px;letter-spacing:.5px}
.card__btn{background:var(--brown);color:var(--white);font-size:14px;padding:5px 10px;letter-spacing:.2px;white-space:nowrap}
.footer{position:absolute;left:0;top:1170px;width:1200px;height:178px;background:var(--green-foot);border-top:5px solid #e3e3e3}
.footer__col{position:absolute;top:18px;color:var(--white);font-size:12px;white-space:nowrap}
.footer__col h3{font-family:"Noto Serif",Georgia,serif;font-style:italic;font-weight:400;font-size:17px;margin-bottom:13px}
.footer__col p{margin-bottom:9px;display:flex;align-items:center;gap:7px}
.follow{display:block;width:139px;height:20px;margin-bottom:14px;background:#2b3a7a;font-family:"Noto Serif",Georgia,serif;font-style:italic;font-size:11px;line-height:20px;padding-left:18px;position:relative;overflow:hidden}
.follow::before{content:"";position:absolute;left:5px;top:5px;width:9px;height:9px;background:var(--white);border-radius:2px}
.follow--b{background:#3a7ac8}.follow--c{background:#222}
.totop{position:absolute;left:1113px;top:1273px;width:35px;height:35px;border-radius:50%;background:#3f7c3a}
.bottombar{position:absolute;left:0;top:1348px;width:1200px;height:29px;background:var(--green-foot-dark);color:var(--white);font-family:"Noto Serif",Georgia,serif;font-style:italic;font-size:13px}
.bottombar__links{position:absolute;left:112px;top:7px;white-space:nowrap}
.bottombar__copy{position:absolute;left:835px;top:0;height:29px;width:365px;background:#3e7238;padding:7px 0 0 14px;font-size:12px;white-space:nowrap}
</style>
</head>
<body>
<div class="site">
  <div class="topbar">
    <div class="topbar__phone">
      <svg width="18" height="18" viewBox="0 0 24 24"><path fill="#fff" d="M6.6 10.8a15 15 0 0 0 6.6 6.6l2.2-2.2c.3-.3.7-.4 1-.2 1.1.4 2.300.6 3.6.6.6 0 1 .4 1 1V20c0 .6-.4 1-1 1A17 17 0 0 1 3 4c0-.6.4-1 1-1h3.5c.6 0 1 .4 1 1 0 1.3.2 2.5.6 3.6.1.3 0 .7-.2 1z"/></svg>
      1800.414.273
    </div>
    <div class="topbar__social"><span></span><span></span><span></span><span></span><span></span></div>
  </div>

  <nav class="nav">
    <a style="left:362px">HOME</a>
    <a style="left:466px">MENU »</a>
    <a style="left:590px">BLOG »</a>
    <a class="is-active" style="left:705px">Product »</a>
    <a style="left:868px">GALLERY »</a>
    <a style="left:1009px">CONTACT</a>
  </nav>

  <div class="brand"><div class="brand__disc">Crest<br>Cellarist</div></div>

  <header class="hero" role="img" aria-label="Rows of oak wine barrels stacked in a cellar">
    <div class="hero__text">
      <div class="hero__line1">Storing,serving and</div>
      <div class="hero__line2">TASTING WINE</div>
    </div>
  </header>

  <div class="breadcrumb">Home / Menu / Products</div>

  <aside class="panel panel--cats">
    <h2>Categories</h2>
    <ul>
      <li>Red Wines</li><li>White Wines</li><li>Pink Wines</li><li>Sparkling</li><li>Sherry &amp; Port</li>
      <li>Wine Collections</li><li>Monthly Wine Clubs</li><li>Glassware</li><li>Wine Accessories</li><li>Food Pairing</li>
    </ul>
  </aside>

  <aside class="panel panel--posts">
    <h2>Recent Posts</h2>
    <ul>
      <li>Simple Style Guide:</li><li>Oatmeal Stout</li><li>What's The Skins Got To</li><li>Do With It?</li>
      <li>5 of My All-Time Favorite</li><li>Homebrew Recipes</li><li>Getting Used Wine Bottles</li>
      <li>Ready For The Wine</li><li>Bottling One-Gallon Batches</li><li>of Beer, Mead, and Cider</li>
    </ul>
  </aside>

  <div class="products-head">
    <h1>Our Products</h1>
    <div class="pager"><span>« PAGE:</span><span>1</span><span>2</span><span>3</span><span>4</span><span>5</span><span>Next »</span></div>
  </div>

  <div class="card" style="left:369px;top:415px"><div class="card__img" role="img" aria-label="Grain mill hopper on a bucket" style="background:linear-gradient(#2a2a2a,#6a6a6a)"></div><p class="card__name">Keelstone® Grain Mill</p><div class="card__foot"><span class="card__price">$279.99</span><span class="card__btn">Add to cart</span></div></div>
  <div class="card" style="left:627px;top:415px"><div class="card__img" role="img" aria-label="Propane burner stand for brewing" style="background:linear-gradient(#8a6a52,#c9b6a4)"></div><p class="card__name">Keelstone® Grain Mill</p><div class="card__foot"><span class="card__price">$279.99</span><span class="card__btn">Add to cart</span></div></div>
  <div class="card" style="left:884px;top:415px"><div class="card__img" role="img" aria-label="Stainless steel immersion chiller coil" style="background:linear-gradient(#e2e4e6,#a8acb0)"></div><p class="card__name">Keelstone® Grain Mill</p><div class="card__foot"><span class="card__price">$279.99</span><span class="card__btn">Add to cart</span></div></div>

  <div class="card" style="left:369px;top:661px"><div class="card__img" role="img" aria-label="Clear plastic fermenter carboy" style="background:linear-gradient(#eef1f4,#cfd6dd)"></div><p class="card__name">Keelstone® Grain Mill</p><div class="card__foot"><span class="card__price">$279.99</span><span class="card__btn">Add to cart</span></div></div>
  <div class="card" style="left:627px;top:661px"><div class="card__img" role="img" aria-label="Rack of amber bottles drying" style="background:linear-gradient(#f0ece6,#7a4a22 50%,#efeae4)"></div><p class="card__name">Keelstone® Grain Mill</p><div class="card__foot"><span class="card__price">$279.99</span><span class="card__btn">Add to cart</span></div></div>
  <div class="card" style="left:884px;top:661px"><div class="card__img" role="img" aria-label="Steel burner with blue flame" style="background:radial-gradient(circle at 50% 35%,#cfe3f5,#8d9196 60%,#5a5d60)"></div><p class="card__name">Keelstone® Grain Mill</p><div class="card__foot"><span class="card__price">$279.99</span><span class="card__btn">Add to cart</span></div></div>

  <div class="card" style="left:369px;top:907px"><div class="card__img" role="img" aria-label="Refractometer in an open case" style="background:linear-gradient(#d8d8d8,#8e8e8e)"></div><p class="card__name">Keelstone® Grain Mill</p><div class="card__foot"><span class="card__price">$279.99</span><span class="card__btn">Add to cart</span></div></div>
  <div class="card" style="left:627px;top:907px"><div class="card__img" role="img" aria-label="Plate wort chiller" style="background:linear-gradient(#f2f2f2,#b5b7b9)"></div><p class="card__name">Keelstone® Grain Mill</p><div class="card__foot"><span class="card__price">$279.99</span><span class="card__btn">Add to cart</span></div></div>
  <div class="card" style="left:884px;top:907px"><div class="card__img" role="img" aria-label="Perforated stainless false bottom" style="background:radial-gradient(circle,#c8c8c8 30%,#1e1e1e 70%)"></div><p class="card__name">Keelstone® Grain Mill</p><div class="card__foot"><span class="card__price">$279.99</span><span class="card__btn">Add to cart</span></div></div>

  <footer class="footer">
    <div class="footer__col" style="left:112px">
      <h3>Contact info:</h3>
      <p><svg width="14" height="12" viewBox="0 0 24 22"><path fill="#fff" d="M12 21 2 11a6 6 0 0 1 10-7 6 6 0 0 1 10 7z"/></svg>Just the best CAKES</p>
      <p><svg width="14" height="14" viewBox="0 0 24 24"><rect x="6" y="2" width="12" height="20" rx="2" fill="none" stroke="#fff" stroke-width="2"/></svg>5412.307.889</p>
      <p><svg width="14" height="12" viewBox="0 0 24 18"><rect x="1" y="1" width="22" height="16" fill="none" stroke="#fff" stroke-width="2"/><path d="M1 1l11 9 11-9" fill="none" stroke="#fff" stroke-width="2"/></svg>hello@crestcellarist.com</p>
      <p><svg width="14" height="14" viewBox="0 0 24 24"><path fill="#fff" d="M12 2a7 7 0 0 0-7 7c0 5 7 13 7 13s7-8 7-13a7 7 0 0 0-7-7zm0 9.5A2.5 2.5 0 1 1 12 6.5a2.5 2.5 0 0 1 0 5z"/></svg>Harbor Lane 14/B</p>
    </div>
    <div class="footer__col" style="left:349px">
      <h3>Work time:</h3>
      <p>Monday - Friday: 8 AM - 8 PM</p><p>Saturday: 9 AM - 4 PM</p><p>Sunday: closed :(</p>
    </div>
    <div class="footer__col" style="left:586px">
      <h3>Become our friend:</h3>
      <span class="follow">follow us on Hearthline</span>
      <span class="follow follow--b">follow us on Chirpwire</span>
      <span class="follow follow--c">follow us on Plusgrid</span>
    </div>
    <div class="footer__col" style="left:825px">
      <h3>Blog - our secret recipes:</h3>
      <p><svg width="14" height="11" viewBox="0 0 14 11"><rect x="1" y="3" width="12" height="7" rx="2" fill="#fff"/></svg>Cake with chocolate &amp; strawberries</p>
      <p><svg width="14" height="11" viewBox="0 0 14 11"><rect x="1" y="3" width="12" height="7" rx="2" fill="#fff"/></svg>Simple vanilla cake</p>
      <p><svg width="14" height="11" viewBox="0 0 14 11"><rect x="1" y="3" width="12" height="7" rx="2" fill="#fff"/></svg>Unusual dark pancakes</p>
    </div>
  </footer>
  <svg class="totop" viewBox="0 0 35 35"><path d="M9 21l8.5-8.5L26 21" fill="none" stroke="#5f9f56" stroke-width="4"/></svg>

  <div class="bottombar">
    <div class="bottombar__links">home&nbsp; / &nbsp;about&nbsp; / &nbsp;our cakes&nbsp; / &nbsp;price&nbsp; / &nbsp;blog&nbsp; / &nbsp;contact</div>
    <div class="bottombar__copy">copyright: crestcellarist.com 2014</div>
  </div>
</div>
</body>
</html>
```